Mortgage Company ready to make a statement!

We have a basic logo that I am fairly happy with ... but it could use a little bit of tweaking before we order the sign for our building. We also want some knock-your-socks-off business cards.
Problem: Inside of our Mortgage Office (Tall Fern Mortgage Group), we are going to have a coffee lounge (Brewnook Cafe) for Realtors to use instead of the local Copperbean to meet with homebuyers. The office and coffee lounge are in an industrial building and is decorated with cozy overstuffed chairs, a hodge podge of interesting lamps and furniture, and goal is to make it as inviting as possible. However, we are a financial institution... so we need to keep it pretty clean as well.
One of my favorite marketing ideas is to cut a house key for everyone who buys a home using us with a key that matches our logo. There's only one key shape that works really well, so that needs to match the logo in order for the idea to work. I'll attach an image of the key blank.... although the way the key hole cut out looks terrible, so I was thinking of having them just do a thin outline instead.
Would like a similar, matching logo for the Brewnook Cafe... but possibly something that would be a little less formal and would be cute on a coffee mug- nothing stuffy.
AND, we're opening a home inspection company as well, and we would like that logo and branding to match. The home inspection company is "Tall Fern Home Inspections"
We were thinking that for the home inspection company , we could use a magnifying glass shape inside of the house shape for the logo, use a keyhole shape inside of the same house for the mortgage company, and use a coffee cup inside of the house shape for Brewnook Cafe.
Just getting stuck and need to help. I designed the attached logo myself, and that is what we are currently using. Designers at local printing companies have failed to impress us.
The mortgage industry has a lot of numbers and logos, etc that they require us to put on our business cards... so it's hard to keep them looking clean.
HELP! HELP! :)

```html
<!DOCTYPE html>
<html lang="en">
<head>
<meta charset="utf-8">
<title>Tall Fern Mortgage Group – Business Cards</title>
<link rel="stylesheet" href="https://fonts.googleapis.com/css2?family=Cinzel:wght@700&family=Josefin+Sans:wght@300&family=Open+Sans:wght@400&display=swap">
<style>
  :root {
    --brand-blue: #236487;
    --brand-blue-dark: #1d5675;
    --card-white: #ffffff;
    --ink: #3a3a3a;
    --backdrop: #ebe8e3;
  }
  * { margin: 0; padding: 0; box-sizing: border-box; }
  html, body {
    width: 1200px; height: 900px; overflow: hidden;
    background: var(--backdrop);
  }
  .stage {
    position: relative; width: 1200px; height: 900px;
  }
  .card {
    position: absolute; left: 280px; width: 640px; height: 366px;
    overflow: hidden;
    box-shadow: 0 6px 18px rgba(0,0,0,0.12);
  }
  .card--front { top: 48px; background: var(--brand-blue); }
  .card--back { top: 486px; background: var(--card-white); }

  .wordmark {
    display: flex; align-items: center; gap: 14px;
    font-family: "Josefin Sans", sans-serif; font-weight: 300;
    letter-spacing: 0.02em; line-height: 1.05;
  }
  .wordmark__dot {
    width: 30px; height: 30px; border-radius: 50%; flex: none;
  }
  .wordmark__name { display: block; }
  .wordmark__name .line-main { display: block; text-transform: uppercase; }
  .wordmark__name .line-sub { display: block; }

  .card--front .wordmark {
    position: absolute; left: 150px; top: 134px; color: var(--card-white);
  }
  .card--front .wordmark__dot { background: var(--card-white); }
  .card--front .line-main { font-size: 52px; }
  .card--front .line-sub { font-size: 30px; padding-left: 30px; }

  .card--back .wordmark {
    position: absolute; left: 58px; top: 50px; color: var(--brand-blue);
  }
  .card--back .wordmark__dot { background: var(--brand-blue); width: 24px; height: 24px; }
  .card--back .line-main { font-size: 42px; }
  .card--back .line-sub { font-size: 24px; padding-left: 24px; }

  .person {
    position: absolute; left: 58px; top: 196px;
  }
  .person__name {
    font-family: "Cinzel", serif; font-weight: 700;
    font-size: 19px; color: var(--brand-blue); letter-spacing: 0.03em;
  }
  .person__title {
    font-family: "Open Sans", sans-serif; font-size: 14px; color: var(--ink);
    margin-top: 2px;
  }
  .contacts {
    position: absolute; left: 58px; top: 250px; list-style: none;
    font-family: "Open Sans", sans-serif; font-size: 15px; color: var(--ink);
  }
  .contacts li { display: flex; align-items: center; gap: 10px; height: 22px; }
  .contacts svg { width: 12px; height: 12px; fill: var(--brand-blue-dark); flex: none; }

  .address {
    position: absolute; right: 26px; top: 262px; text-align: right;
    font-family: "Open Sans", sans-serif; font-size: 12.5px; color: var(--ink);
    line-height: 1.45;
  }
  .band {
    position: absolute; left: 0; right: 0; bottom: 0; height: 22px;
    background: var(--brand-blue);
  }
</style>
</head>
<body>
<main class="stage">

  <section class="card card--front" aria-label="Card front">
    <div class="wordmark">
      <span class="wordmark__dot"></span>
      <span class="wordmark__name">
        <span class="line-main">Tall Fern</span>
        <span class="line-sub">Mortgage Group</span>
      </span>
    </div>
  </section>

  <section class="card card--back" aria-label="Card back">
    <div class="wordmark">
      <span class="wordmark__dot"></span>
      <span class="wordmark__name">
        <span class="line-main">Tall Fern</span>
        <span class="line-sub">Mortgage Group</span>
      </span>
    </div>

    <div class="person">
      <p class="person__name">DANIEL HARROW</p>
      <p class="person__title">Managing Director</p>
    </div>

    <ul class="contacts">
      <li>
        <svg viewBox="0 0 24 24" aria-hidden="true"><path d="M6.6 10.8a15.1 15.1 0 0 0 6.6 6.6l2.2-2.2a1 1 0 0 1 1-.25 11.4 11.4 0 0 0 3.6.57 1 1 0 0 1 1 1V20a1 1 0 0 1-1 1A17 17 0 0 1 3 4a1 1 0 0 1 1-1h3.5a1 1 0 0 1 1 1c0 1.25.2 2.45.57 3.57a1 1 0 0 1-.25 1z"/></svg>
        (044)578201346
      </li>
      <li>
        <svg viewBox="0 0 24 24" aria-hidden="true"><path d="M2 5h20v14H2z M2 5l10 8 10-8" fill="none" stroke="#1d5675" stroke-width="0"/><path d="M2 5h20v2l-10 7L2 7z"/><path d="M2 9l10 7 10-7v10H2z"/></svg>
        hello@tallfernmail.com
      </li>
      <li>
        <svg viewBox="0 0 24 24" aria-hidden="true"><circle cx="12" cy="12" r="10"/><path d="M2 12h20M12 2c3 3 3 17 0 20M12 2c-3 3-3 17 0 20" fill="none" stroke="#fff" stroke-width="1.4"/></svg>
        www.tallfernloans.com
      </li>
    </ul>

    <p class="address">4821, Fernway Lane,<br>Country name, 12345</p>

    <div class="band"></div>
  </section>

</main>
</body>
</html>
```